Website redesign

We need a bold revamp of our website (http://www.brantwoodpower.co.nz/)
which at the moment looks dated. We want a crisp, fresh and bold look. The background image behind web page can go. Open to complete new layout

Target Market(s)

Electrical contracting company- working in the domestic and commercial field

Coding

Coded - Design and coding required

Number of Pages Required

5+ page

Font styles to use
Sans Serif

Colors

Designer to choose colors to be used in the design.

```html
<!DOCTYPE html>
<html lang="en">
<head>
<meta charset="utf-8">
<title>Brantwood Power</title>
<link href="https://fonts.googleapis.com/css2?family=Open+Sans:wght@300;400;600;700&display=swap" rel="stylesheet">
<style>
:root{
  --red:#ee1c1c;
  --red-dark:#c70f0f;
  --ink:#111;
  --text:#333;
  --muted:#777;
  --light:#f2f2f2;
  --white:#fff;
  --dark:#1d1f22;
  --slate:#3b4a55;
}
*{margin:0;padding:0;box-sizing:border-box}
html,body{width:1200px;height:2778px;overflow:hidden}
body{position:relative;font-family:"Open Sans",Arial,sans-serif;color:var(--text);background:var(--white)}
.abs{position:absolute}
.btn{position:absolute;display:flex;align-items:center;justify-content:center;height:30px;background:var(--red);color:var(--white);font-size:11px;clip-path:polygon(8% 0,92% 0,100% 50%,92% 100%,8% 100%,0 50%)}
.btn.dark{background:var(--ink)}

/* header */
.site-header{left:0;top:0;width:1200px;height:74px;background:rgba(40,40,40,.55);z-index:5}
.brand{left:0;top:0;width:178px;height:74px;background:var(--white);clip-path:polygon(0 0,100% 0,84% 100%,0 100%);display:flex;align-items:center;padding-left:18px;gap:8px}
.brand-mark{width:14px;height:14px;background:var(--red)}
.brand-name{font-size:17px;font-weight:700;color:var(--ink);line-height:1}
.nav{left:340px;top:26px;display:flex;gap:0}
.nav a{position:absolute;font-size:12.5px;color:var(--white);text-decoration:none;white-space:nowrap}
.nav a.active{color:var(--red)}
.phone-box{left:870px;top:0;width:330px;height:74px;background:var(--red);clip-path:polygon(6% 0,100% 0,100% 100%,0 100%)}
.phone-box svg{position:absolute;left:36px;top:20px}
.phone-box .lbl{position:absolute;left:82px;top:17px;font-size:10px;color:var(--white)}
.phone-box .num{position:absolute;left:82px;top:32px;font-size:15px;color:var(--white)}

/* hero */
.hero{left:0;top:0;width:1200px;height:565px;background:linear-gradient(100deg,#c9b8ad 0%,#e9e6e2 35%,#f4f3f1 60%,#d9d6d2 100%)}
.hero-caption{left:293px;top:296px;width:611px;height:148px;background:rgba(40,40,40,.72);border:2px solid var(--red);text-align:center;color:var(--white)}
.hero-caption h1{font-weight:400;font-size:38px;margin-top:26px;letter-spacing:.5px}
.hero-caption p{font-size:11px;line-height:15px;width:480px;margin:8px auto 0}

/* welcome */
.welcome{left:0;top:565px;width:1200px;height:367px;background:linear-gradient(90deg,#f4f4f4,#ececec)}
.welcome-photo{left:696px;top:565px;width:504px;height:367px;background:linear-gradient(90deg,#d9d9d9,#8d8d8d)}
.welcome h2{position:absolute;left:230px;top:43px;font-size:42px;font-weight:400;color:var(--ink)}
.welcome .copy{position:absolute;left:230px;top:98px;width:380px;font-size:11px;line-height:15px;color:var(--text)}
.welcome .copy p{margin-bottom:12px}

/* sections */
.section-title{position:absolute;width:1200px;left:0;text-align:center;font-size:40px;font-weight:400;color:var(--ink)}
.service{position:absolute;width:192px;text-align:center}
.service .pic{width:192px;height:119px}
.service h3{font-size:14px;font-weight:400;color:var(--ink);margin-top:20px}
.service p{font-size:11px;line-height:16px;margin-top:10px}
.service.featured{background:var(--white);box-shadow:0 18px 30px rgba(0,0,0,.28);border-bottom:4px solid var(--red);padding:4px 20px 0}
.rule{position:absolute;top:1383px;height:3px;background:var(--ink)}

/* projects */
.projects{left:0;top:1559px;width:1200px;height:348px;background:linear-gradient(180deg,#2f3b44,#51636f 60%,#3e4d57)}
.projects .section-title{color:var(--white)}
.projects .sub{position:absolute;width:1200px;top:127px;text-align:center;font-size:11px;color:var(--white)}
.slide{left:294px;top:1741px;width:612px;height:328px;background:linear-gradient(180deg,#c8d6e2 0%,#d9cfc0 35%,#9b7b6a 60%,#6a6a6a 85%,#8b8b8b 100%)}
.slide-caption{left:393px;top:1846px;width:416px;height:115px;background:rgba(40,40,40,.72);border:2px solid var(--red-dark);color:var(--white);text-align:center}
.slide-caption h3{font-size:20px;font-weight:400;margin-top:20px}
.slide-caption p{font-size:11px;line-height:15px;width:340px;margin:12px auto 0}
.dots{left:580px;top:2098px;display:flex;gap:6px}
.dots span{width:10px;height:10px;border-radius:50%;border:1.5px solid var(--red)}
.dots span.on{background:var(--red)}

/* quick links */
.links-col{position:absolute;top:2320px;list-style:none}
.links-col li{font-size:11px;color:var(--muted);height:22.8px;position:relative;padding-left:14px}
.links-col li::before{content:"";position:absolute;left:0;top:5px;width:6px;height:6px;border:1.5px solid var(--red);border-radius:50%}

/* footer */
.contact-band{left:0;top:2528px;width:1200px;height:204px;background:linear-gradient(90deg,#2a2c2f,#1a1b1d 50%,#3a3834)}
.contact-item{position:absolute;top:38px;width:200px;text-align:center;color:var(--white)}
.contact-item .icon{width:66px;height:66px;border-radius:50%;background:var(--white);margin:0 auto;display:flex;align-items:center;justify-content:center}
.contact-item strong{display:block;font-size:12px;font-weight:600;margin-top:12px}
.contact-item span{display:block;font-size:11px;line-height:14px}
.legal{left:0;top:2732px;width:1200px;height:46px;background:var(--red);color:var(--white);font-size:11px}
.legal .copy{position:absolute;left:222px;top:15px}
.legal .auth{position:absolute;left:685px;top:15px}
.badge{position:absolute;top:8px;height:30px;background:var(--white)}
</style>
</head>
<body>

<div class="abs hero" role="img" aria-label="Close-up photo of a hand testing a switchboard with a red multimeter probe"></div>

<header class="abs site-header">
  <div class="abs brand"><span class="brand-mark"></span><span class="brand-name">Brantwood Power</span></div>
  <nav class="abs nav">
    <a class="active" style="left:14px">Home</a>
    <a style="left:92px">About Us</a>
    <a style="left:178px">Services</a>
    <a style="left:260px">Projects</a>
    <a style="left:316px;left:317px">Contact Us</a>
    <a style="left:427px">Info</a>
  </nav>
  <div class="abs phone-box">
    <svg width="30" height="30" viewBox="0 0 24 24" fill="none" stroke="#fff" stroke-width="1.8"><path d="M5 3h4l2 5-2.5 1.5a11 11 0 0 0 6 6L16 13l5 2v4a2 2 0 0 1-2 2A17 17 0 0 1 3 5a2 2 0 0 1 2-2z"/></svg>
    <span class="lbl">Freephone</span>
    <span class="num">0800 41 27 90 or (06) 355 2190</span>
  </div>
</header>

<div class="abs hero-caption">
  <h1>SECURITY CAMERAS</h1>
  <p>Trust the specialist security technicians at Brantwood Power to design, install, support and maintain a surveillance system that covers as much or as little as you need at you home or business.</p>
</div>
<a class="btn" style="left:543px;top:429px;width:115px">Read More</a>

<section class="abs welcome">
  <h2>WELCOME</h2>
  <div class="copy">
    <p>Brantwood Power is a leading electrical installation and maintenance company based in Wanganui, but servicing all New Zealand.</p>
    <p>With over 15 professionally qualified and experienced Wanganui electricians, technicians and support staff we are leading the way in providing quality electrical services.</p>
    <p>Brantwood Power was established in 1991 and does it all, from supplying and changing light bulbs, comprehensive whole house electrical design and installation, to commercial and large scale industrial consultation, implementation and servicing.</p>
  </div>
</section>
<div class="abs welcome-photo" role="img" aria-label="Photo of a white wall-mounted security camera"></div>
<a class="btn" style="left:230px;top:850px;width:181px">Click to Read More About Us...</a>

<h2 class="section-title" style="top:992px">OUR SERVICES</h2>

<div class="service" style="left:252px;top:1074px">
  <div class="pic" role="img" aria-label="Photo of an electrician wiring a switchboard" style="background:linear-gradient(135deg,#c9d3df,#6f8fb8 60%,#d44)"></div>
  <h3>ELECTRICAL</h3>
  <p>Lorem ipsum dolor sit amet, consectetur adipiscing elit. Mauris at fringilla nibh. Morbi nec erat placerat, sodales libero vitae, fringilla arcu.</p>
</div>
<div class="service featured" style="left:485px;top:1070px;width:232px;height:315px">
  <div class="pic" role="img" aria-label="Photo of a modern kitchen with stainless appliances" style="background:linear-gradient(180deg,#e6e6e6,#8a8f96 55%,#5d6670)"></div>
  <h3>APPLIANCES</h3>
  <p>Lorem ipsum dolor sit amet, consectetur adipiscing elit. Mauris at fringilla nibh. Morbi nec erat placerat, sodales libero vitae, fringilla arcu.</p>
</div>
<div class="service" style="left:756px;top:1074px">
  <div class="pic" role="img" aria-label="Photo of a ceiling smoke alarm" style="background:radial-gradient(circle at 45% 45%,#f2f2f2 0,#cfcfcf 35%,#8b2a2a 75%,#3a1010)"></div>
  <h3>ALARMS</h3>
  <p>Lorem ipsum dolor sit amet, consectetur adipiscing elit. Mauris at fringilla nibh. Morbi nec erat placerat, sodales libero vitae, fringilla arcu.</p>
</div>
<a class="btn" style="left:285px;top:1330px;width:126px">Read More</a>
<a class="btn dark" style="left:538px;top:1330px;width:126px">Read More</a>
<a class="btn" style="left:790px;top:1330px;width:126px">Read More</a>
<div class="rule" style="left:231px;width:254px"></div>
<div class="rule" style="left:717px;width:250px"></div>
<a class="btn" style="left:544px;top:1452px;width:124px">View All</a>

<section class="abs projects" role="img" aria-label="Background photo of a satellite dish against a cloudy sky">
  <h2 class="section-title" style="top:64px">OUR PROJECTS</h2>
  <p class="sub">Here are just a few of our more recent major projects Brantwood Power has completed -</p>
</section>
<div class="abs slide" role="img" aria-label="Photo of a two-storey commercial building with cars parked in front"></div>
<div class="abs slide-caption">
  <h3>CIVIC BUILDING - NEW BUILD</h3>
  <p>Civic Building - Everything Electrical as well as installation of specialised security system.</p>
</div>
<div class="abs dots"><span class="on"></span><span></span><span></span></div>
<a class="btn" style="left:537px;top:2148px;width:126px">View All</a>

<h2 class="section-title" style="top:2242px">QUICK LINKS</h2>
<ul class="links-col" style="left:222px">
  <li>Residential Electrical</li><li>Commercial Electrical</li><li>Kaimai Heat Pumps</li><li>Fire Alarms</li><li>Security Cameras</li><li>Hot Water Cylinders</li>
</ul>
<ul class="links-col" style="left:419px">
  <li>CCTV Cameras</li><li>Interior Lighting</li><li>Exterior Lighting</li><li>Smoke Detectors</li><li>Air Conditioners</li><li>Free to View TV</li>
</ul>
<ul class="links-col" style="left:611px">
  <li>Satellite Dish</li><li>UHF Aerials</li><li>Home Security</li><li>Appliance repairs</li><li>Electrical testing &amp; tagging</li><li>Phone and Data</li>
</ul>
<ul class="links-col" style="left:807px">
  <li>Electrical Inspections</li><li>Ventilation</li><li>Hot Water Heatpumps</li><li>Heat Recovery Systems</li><li>Thermal Imaging</li>
</ul>

<footer>
  <div class="abs contact-band" role="img" aria-label="Dark background photo of an electrician at a switchboard">
    <div class="contact-item" style="left:226px">
      <div class="icon"><svg width="26" height="26" viewBox="0 0 24 24" fill="#ee1c1c"><path d="M12 2a7 7 0 0 0-7 7c0 5 7 13 7 13s7-8 7-13a7 7 0 0 0-7-7zm0 9.5A2.5 2.5 0 1 1 12 6.5a2.5 2.5 0 0 1 0 5z"/></svg></div>
      <strong>Location</strong><span>14 Kerrow Road, Wanganui 4500</span>
    </div>
    <div class="contact-item" style="left:417px">
      <div class="icon"><svg width="26" height="26" viewBox="0 0 24 24" fill="none" stroke="#ee1c1c" stroke-width="2"><path d="M5 3h4l2 5-2.5 1.5a11 11 0 0 0 6 6L16 13l5 2v4a2 2 0 0 1-2 2A17 17 0 0 1 3 5a2 2 0 0 1 2-2z"/></svg></div>
      <strong>Phone</strong><span>0800 41 27 90</span><span>(06) 355 2190</span>
    </div>
    <div class="contact-item" style="left:585px">
      <div class="icon"><svg width="26" height="26" viewBox="0 0 24 24" fill="#ee1c1c"><rect x="6" y="3" width="12" height="6"/><rect x="3" y="10" width="18" height="8" rx="1"/><rect x="7" y="15" width="10" height="6" fill="#fff" stroke="#ee1c1c" stroke-width="1.5"/></svg></div>
      <strong>Fax</strong><span>Fax: (06) 355 2191</span>
    </div>
    <div class="contact-item" style="left:772px">
      <div class="icon"><svg width="26" height="26" viewBox="0 0 24 24"><rect x="3" y="5" width="18" height="14" fill="#ee1c1c"/><path d="M3 5l9 8 9-8" fill="none" stroke="#fff" stroke-width="1.6"/></svg></div>
      <strong>Email</strong><span>office@brantwoodpower.co.nz</span>
    </div>
  </div>
  <div class="abs legal">
    <span class="copy">Copyright (c) 2018 , Brantwood Power. All Rights Reserved.</span>
    <span class="auth">We are authorised installers for:</span>
    <div class="badge" style="left:856px;width:62px"></div>
    <div class="badge" style="left:922px;width:56px"></div>
  </div>
</footer>

</body>
</html>
```